Management Consulting needing a cool business card for client acquisition and networking

We are looking for a business card that is progressive and fresh that conveys innovation, forward thinking, and confidence. The business card is for a company based in Charlotte NC called, 'MERIDOX CONSULTING GROUP LLC'. The company primarily works with banks, insurance, and brokerages to implement innovative solutions to help them streamline their operations, to more effectively manage risks, and to improve their customer relationships.

Target Market(s)

Typically meet with Chief Financial Officers, Chief Information Officers, Chief Operations Officer, Business Unit Leader. The target market are generally 40-55 years, male, white, master level education plus.

Industry/Entity Type

Progressive

Font styles to use
Serif
Other font styles liked:
• Calibri

Requirements
Should not have
• Designs that look too much like law firms or accounting companies. Too conservative

```html
<!DOCTYPE html>
<html lang="en">
<head>
<meta charset="utf-8">
<title>Meridox Consulting Group LLC – Business Card</title>
<link href="https://fonts.googleapis.com/css2?family=Michroma&display=swap" rel="stylesheet">
<style>
  :root {
    --page: #ffffff;
    --card: #fcbd2a;
    --ink: #ffffff;
  }
  * { margin: 0; padding: 0; box-sizing: border-box; }
  html, body { width: 1200px; height: 1000px; overflow: hidden; background: var(--page); }
  body { position: relative; font-family: "Michroma", "Verdana", sans-serif; color: var(--ink); }

  .card { position: absolute; background: var(--card); overflow: hidden; }
  .card--front { left: 121px; top: 164px; width: 495px; height: 283px; }
  .card--back  { left: 130px; top: 563px; width: 505px; height: 288px; }
  .card--mark  { left: 722px; top: 294px; width: 358px; height: 430px; }

  .rule { position: absolute; background: var(--ink); height: 2px; }
  .rule--v { width: 2px; }

  .text { position: absolute; white-space: nowrap; font-variant: small-caps; line-height: 1; color: var(--ink); }

  .deco-ring {
    position: absolute; border-radius: 50%;
    border: 11px solid var(--ink); background: var(--card);
  }

  .brand-name {
    position: absolute; display: flex; align-items: center; justify-content: center;
    gap: 8px; white-space: nowrap; line-height: 1; color: var(--ink);
    font-family: "Michroma", "Verdana", sans-serif;
  }
  .brand-name__dot { display: block; border-radius: 50%; background: var(--ink); flex: none; }

  /* front */
  .front__company   { left: 179px; top: 26px; font-size: 17px; letter-spacing: 2px; }
  .front__company-2 { left: 248px; top: 56px; font-size: 17px; letter-spacing: 2px; }
  .front__name   { left: 72px; top: 137px; font-size: 18px; letter-spacing: 1px; }
  .front__title  { left: 33px; top: 161px; font-size: 13px; letter-spacing: 1.6px; }
  .front__street { left: 32px; top: 207px; font-size: 12px; letter-spacing: 1px; }
  .front__city   { left: 69px; top: 229px; font-size: 12px; letter-spacing: 1.5px; }
  .front__office { left: 33px; top: 266px; font-size: 11px; letter-spacing: 0.6px; }
  .front__cell   { left: 306px; top: 266px; font-size: 11px; letter-spacing: 0.6px; }

  /* back */
  .back__web { left: 10px; top: 118px; font-size: 13px; letter-spacing: 2.4px; }
</style>
</head>
<body>

<section class="card card--front" aria-label="Business card front">
  <div class="rule" style="left:0; top:50px; width:495px;"></div>
  <div class="deco-ring" style="left:66px; top:15px; width:78px; height:78px;"></div>

  <p class="text front__company">Meridox Consulting</p>
  <p class="text front__company-2">Group LLC</p>

  <div class="rule" style="left:41px; top:189px; width:290px;"></div>
  <div class="rule" style="left:460px; top:189px; width:35px;"></div>
  <div class="brand-name" style="left:331px; top:150px; width:126px; height:30px; font-size:16px;">
    <span class="brand-name__dot" style="width:10px; height:10px;"></span>Meridox
  </div>

  <p class="text front__name">Colin R. Vance</p>
  <p class="text front__title">Chief Solutions Architect</p>
  <p class="text front__street">2715 Lakeside Rd., Suite 300</p>
  <p class="text front__city">Charlotte, NC 28277</p>

  <div class="rule" style="left:0; top:259px; width:495px;"></div>
  <div class="rule rule--v" style="left:235px; top:259px; bottom:0;"></div>
  <p class="text front__office">o : 704-555-0142</p>
  <p class="text front__cell">c : 704-555-0187</p>
</section>

<section class="card card--back" aria-label="Business card back">
  <p class="text back__web">www.meridoxconsulting.com</p>
  <div class="rule" style="left:0; top:156px; width:322px;"></div>
  <div class="rule" style="left:458px; top:156px; width:47px;"></div>
  <div class="brand-name" style="left:324px; top:120px; width:132px; height:30px; font-size:16px;">
    <span class="brand-name__dot" style="width:10px; height:10px;"></span>Meridox
  </div>
</section>

<section class="card card--mark" aria-label="Brand name panel">
  <div class="brand-name" style="left:0; top:190px; width:358px; height:50px; font-size:30px; gap:14px;">
    <span class="brand-name__dot" style="width:18px; height:18px;"></span>Meridox
  </div>
</section>

</body>
</html>
```